Facebook AD
Marlow Heating Cooling & Plumbing
Facebook AD - Trade
Creative Brief
Bright & Fun-filled
not a business card. no name needed
NA
marlowhvacbrenton@examplemail.test
I want to design a Facebook type of ad/flyer/banner I want the logo, and phone number listed on there. The point, and main text of the ad should read "Why choose us?" With the following points made. Affordable Free estimates & Second opinions No pressure quoting - no scare tactics 24/7 Emergency service - no after hours fee Locally owned and operated Interest free financing Customer satisfaction guaranteed 5-Star rated I don't really want them just in a list, something eye catching, with our logo, something repair or related to heating cooling plumbing work maybe in the background or in some photos off to the side.

```html
<!DOCTYPE html>
<html lang="en">
<head>
<meta charset="utf-8">
<title>Marlow Heating Cooling &amp; Plumbing – Facebook Ad</title>
<link rel="stylesheet" href="https://fonts.googleapis.com/css2?family=Oswald:wght@400;500;600&display=swap">
<style>
  :root {
    --page: #eeeeee;
    --ink: #0c0c0d;
    --charcoal: #1b1d20;
    --blue: #1b8bd2;
    --blue-light: #43b0ea;
    --blue-deep: #0d5a97;
    --white: #ffffff;
  }
  * { margin: 0; padding: 0; box-sizing: border-box; }
  html, body { width: 1200px; height: 1042px; overflow: hidden; background: var(--page); }
  body { position: relative; font-family: "Oswald", sans-serif; color: var(--white); }

  .ad-banner {
    position: absolute; left: 50px; top: 315px; width: 1100px; height: 412px;
    overflow: hidden;
  }
  .ad-background { position: absolute; inset: 0; width: 100%; height: 100%; }

  .brand { position: absolute; left: 70px; top: 118px; width: 420px; text-align: center; }
  .brand-name {
    font-weight: 500; font-size: 104px; line-height: 1; letter-spacing: 2px;
    color: var(--white); display: flex; align-items: center; justify-content: center; gap: 14px;
  }
  .brand-dot { width: 22px; height: 22px; border-radius: 50%; background: var(--blue-light); flex: none; }
  .brand-tagline {
    margin-top: 10px; padding-top: 8px; border-top: 2px solid var(--white);
    font-size: 22px; font-weight: 400; letter-spacing: 2px; white-space: nowrap;
  }

  .phone {
    position: absolute; left: 34px; top: 302px; display: flex; align-items: center; gap: 16px;
  }
  .phone-icon { width: 40px; height: 40px; }
  .phone-number { font-size: 44px; font-weight: 500; letter-spacing: 3px; line-height: 1; }

  .reasons-title {
    position: absolute; right: 34px; top: 30px;
    font-size: 40px; font-weight: 600; letter-spacing: 1.5px; line-height: 1;
  }
  .reasons {
    position: absolute; right: 34px; top: 112px; list-style: none; text-align: right;
  }
  .reasons li {
    font-size: 22px; font-weight: 500; letter-spacing: 1.2px; line-height: 33px; text-transform: uppercase;
  }
  .stars { letter-spacing: 3px; margin-right: 8px; }
</style>
</head>
<body>
  <section class="ad-banner" aria-label="Marlow Heating Cooling &amp; Plumbing advert">
    <svg class="ad-background" viewBox="0 0 1100 412" preserveAspectRatio="none" aria-hidden="true">
      <defs>
        <linearGradient id="left-panel" x1="0" y1="0" x2="1" y2="0">
          <stop offset="0" stop-color="#0c0c0d"/>
          <stop offset="0.45" stop-color="#121a24"/>
          <stop offset="1" stop-color="#1470b3"/>
        </linearGradient>
        <linearGradient id="right-panel" x1="0" y1="0" x2="1" y2="1">
          <stop offset="0" stop-color="#1579c0"/>
          <stop offset="0.6" stop-color="#1b8bd2"/>
          <stop offset="1" stop-color="#0d5a97"/>
        </linearGradient>
        <linearGradient id="phone-bar" x1="0" y1="0" x2="1" y2="0">
          <stop offset="0" stop-color="#1b8bd2"/>
          <stop offset="1" stop-color="#0f64a6"/>
        </linearGradient>
      </defs>
      <rect width="1100" height="412" fill="url(#right-panel)"/>
      <polygon points="0,0 560,0 600,412 0,412" fill="url(#left-panel)"/>
      <rect width="1100" height="18" fill="var(--ink)"/>
      <polygon points="620,18 1100,18 1100,90 650,90" fill="var(--charcoal)"/>
      <polygon points="0,290 470,290 510,355 0,355" fill="url(#phone-bar)"/>
      <polygon points="505,300 600,300 606,310 511,310" fill="var(--white)"/>
      <polygon points="515,316 740,316 746,326 521,326" fill="var(--white)"/>
      <rect y="382" width="1100" height="30" fill="var(--ink)"/>
    </svg>

    <div class="brand">
      <div class="brand-name"><span class="brand-dot"></span>MARLOW</div>
      <div class="brand-tagline">HEATING • COOLING • PLUMBING</div>
    </div>

    <div class="phone">
      <svg class="phone-icon" viewBox="0 0 40 40" aria-hidden="true">
        <circle cx="20" cy="20" r="19" fill="var(--white)"/>
        <path d="M14 10c1-1 2.4-.8 3 .4l2 4c.4.9.2 1.8-.5 2.4l-1.4 1.2c1 2.2 2.7 3.9 4.9 4.9l1.2-1.4c.6-.7 1.5-.9 2.4-.5l4 2c1.2.6 1.4 2 .4 3l-2 2c-1.3 1.3-3.3 1.5-5 .6-4.8-2.4-8.6-6.2-11-11-.9-1.7-.7-3.7.6-5z" fill="var(--blue)"/>
      </svg>
      <span class="phone-number">5550148823</span>
    </div>

    <h2 class="reasons-title">WHY CHOOSE US?</h2>
    <ul class="reasons">
      <li>Free estimates &amp; second opinions</li>
      <li>No pressure quoting – no scare tactics</li>
      <li>24/7 emergency service – no after hours fee</li>
      <li>Locally owned and operated</li>
      <li>Interest free financing</li>
      <li>Customer satisfaction guaranteed</li>
      <li><span class="stars">★★★★★</span>5-star rated</li>
    </ul>
  </section>
</body>
</html>
```